New signage for apartment community in the Pacific Northwest

Signage for an apartment community in the Pacific Northwest. It should have a contemporary northwest vibe with a fresh exciting feeling. We are open to the colors cayenne, white, charcoal and a splash of lime green. Sign to have the name 'VELTO' with the address number 28391 smaller underneath. sign can include a shape under the name or a feeling of energy in the shape of the name.

Target Market(s)

Young urban professionals

Industry/Entity Type

Real Estate Development

Requirements
Must have
• eyecatching
Should not have
• anything too cute or too busy

```html
<!DOCTYPE html>
<html lang="en">
<head>
<meta charset="utf-8">
<title>VELTO signage concepts</title>
<link rel="stylesheet" href="https://fonts.googleapis.com/css2?family=Playfair+Display:wght@400;500&family=Poppins:wght@300&display=swap">
<style>
  :root {
    --page: #161616;
    --charcoal: #0b0b0b;
    --charcoal-soft: #1e1e1e;
    --lime: #39ff14;
    --cayenne: #6b0a00;
    --white: #ffffff;
    --label: #7a7a7a;
    --shadow: #3a3a3a;
  }
  * { margin: 0; padding: 0; box-sizing: border-box; }
  html, body { width: 848px; height: 1200px; overflow: hidden; background: var(--page); }
  .board { position: relative; width: 848px; height: 1200px; }
  .board-title {
    position: absolute; top: 40px; left: 0; width: 848px;
    text-align: center; color: var(--white);
    font: 300 21px/26px "Poppins", sans-serif;
  }
  .sample-label {
    position: absolute; left: 105px;
    color: var(--label); font: 300 20px/24px "Poppins", sans-serif;
  }
  .sample-label.first { top: 142px; }
  .sample-label.second { top: 1131px; left: 102px; }
  .sign { position: absolute; left: 105px; width: 652px; height: 434px; display: block; }
  .sign.lime-frame { top: 185px; }
  .sign.cayenne-frame { top: 682px; }
  .sign-name { font-family: "Playfair Display", serif; font-weight: 400; font-size: 180px; }
  .sign-number { font-family: "Playfair Display", serif; font-weight: 500; font-size: 38px; letter-spacing: 6px; }
</style>
</head>
<body>
<main class="board">
  <h1 class="board-title">New signage for apartment community in the Pacific<br>Northwest</h1>

  <p class="sample-label first">Sample 1</p>

  <svg class="sign lime-frame" viewBox="0 0 652 434" aria-label="VELTO sign, silver on charcoal with lime frame">
    <defs>
      <radialGradient id="slate-a" cx="55%" cy="55%" r="70%">
        <stop offset="0" stop-color="#1e1e1e"/>
        <stop offset="1" stop-color="#0b0b0b"/>
      </radialGradient>
      <linearGradient id="silver" x1="0" y1="0" x2="0" y2="1">
        <stop offset="0" stop-color="#ffffff"/>
        <stop offset="0.35" stop-color="#f4f4f4"/>
        <stop offset="0.48" stop-color="#a9a9a9"/>
        <stop offset="0.62" stop-color="#f6f6f6"/>
        <stop offset="1" stop-color="#ffffff"/>
      </linearGradient>
      <radialGradient id="flourish-lime" cx="50%" cy="50%" r="50%">
        <stop offset="0" stop-color="#39ff14" stop-opacity="0.55"/>
        <stop offset="1" stop-color="#39ff14" stop-opacity="0"/>
      </radialGradient>
    </defs>
    <rect class="frame" width="652" height="434" fill="var(--lime)"/>
    <rect class="panel" x="16" y="11" width="620" height="412" rx="31" fill="url(#slate-a)"/>
    <g class="rules" stroke="var(--lime)" stroke-width="1.5">
      <line x1="71" y1="82" x2="175" y2="82"/><line x1="480" y1="82" x2="582" y2="82"/>
      <line x1="71" y1="302" x2="175" y2="302"/><line x1="480" y1="302" x2="582" y2="302"/>
    </g>
    <rect x="195" y="47" width="262" height="55" rx="27" fill="url(#flourish-lime)" role="img" aria-label="Ornamental scroll flourish above the name"/>
    <rect x="195" y="276" width="262" height="55" rx="27" fill="url(#flourish-lime)" role="img" aria-label="Ornamental scroll flourish below the name"/>
    <text class="sign-name" x="80" y="257" textLength="507" lengthAdjust="spacing" fill="var(--shadow)">VELTO</text>
    <text class="sign-name" x="75" y="254" textLength="507" lengthAdjust="spacing" fill="url(#silver)">VELTO</text>
    <text class="sign-number" x="326" y="395" text-anchor="middle" fill="var(--white)">#28391</text>
  </svg>

  <svg class="sign cayenne-frame" viewBox="0 0 652 434" aria-label="VELTO sign, lime on charcoal with cayenne frame">
    <defs>
      <radialGradient id="slate-b" cx="55%" cy="55%" r="70%">
        <stop offset="0" stop-color="#1e1e1e"/>
        <stop offset="1" stop-color="#0b0b0b"/>
      </radialGradient>
      <radialGradient id="flourish-white" cx="50%" cy="50%" r="50%">
        <stop offset="0" stop-color="#ffffff" stop-opacity="0.5"/>
        <stop offset="1" stop-color="#ffffff" stop-opacity="0"/>
      </radialGradient>
    </defs>
    <rect class="frame" width="652" height="434" fill="var(--cayenne)"/>
    <rect class="panel" x="16" y="11" width="620" height="412" rx="31" fill="url(#slate-b)"/>
    <g class="rules" stroke="var(--white)" stroke-width="1.5">
      <line x1="71" y1="82" x2="175" y2="82"/><line x1="480" y1="82" x2="582" y2="82"/>
      <line x1="71" y1="302" x2="175" y2="302"/><line x1="480" y1="302" x2="582" y2="302"/>
    </g>
    <rect x="195" y="47" width="262" height="55" rx="27" fill="url(#flourish-white)" role="img" aria-label="Ornamental scroll flourish above the name"/>
    <rect x="195" y="276" width="262" height="55" rx="27" fill="url(#flourish-white)" role="img" aria-label="Ornamental scroll flourish below the name"/>
    <text class="sign-name" x="80" y="257" textLength="507" lengthAdjust="spacing" fill="var(--shadow)">VELTO</text>
    <text class="sign-name" x="75" y="254" textLength="507" lengthAdjust="spacing" fill="var(--lime)">VELTO</text>
    <text class="sign-number" x="326" y="395" text-anchor="middle" fill="var(--lime)">#28391</text>
  </svg>

  <p class="sample-label second">Sample 2</p>
</main>
</body>
</html>
```